We need a logo for our business which is a dental clinic (i.e. dentistry).
We would lilke designs using the colour blue, green and black incorporating the words Corvasta Dental, possibly a smile or a tooth image can be considered for incorporation in the logo.

Industry/Entity Type

Dental

```html
<!DOCTYPE html>
<html lang="en">
<head>
<meta charset="utf-8">
<title>Corvasta Dental – Business Card</title>
<link href="https://fonts.googleapis.com/css2?family=Noto+Sans:wght@400;500&display=swap" rel="stylesheet">
<style>
  :root {
    --page-bg: #e9ecef;
    --card-blue: #29a3dc;
    --card-blue-mid: #8fd0ee;
    --card-white: #ffffff;
    --ink: #111418;
    --name-blue: #1f95d1;
    --mark-blue: #ffffff;
    --watermark: #e4f3fb;
  }
  * { margin: 0; padding: 0; box-sizing: border-box; }
  html, body {
    width: 1200px;
    height: 900px;
    overflow: hidden;
    background: var(--page-bg);
    font-family: "Noto Sans", Verdana, sans-serif;
  }
  .business-card {
    position: absolute;
    left: 125px;
    top: 193px;
    width: 950px;
    height: 514px;
    overflow: hidden;
    background: linear-gradient(115deg, var(--card-blue) 0%, var(--card-blue-mid) 38%, var(--card-white) 72%, var(--card-white) 100%);
    box-shadow: 0 12px 30px rgba(0, 0, 0, 0.18);
  }
  .background-shape {
    position: absolute;
    right: 40px;
    top: 150px;
    width: 300px;
    height: 300px;
    border-radius: 50%;
    background: var(--watermark);
    opacity: 0.7;
  }
  .brand {
    position: absolute;
    left: 108px;
    top: 78px;
    display: flex;
    align-items: center;
    gap: 22px;
  }
  .brand-mark {
    width: 58px;
    height: 58px;
    border-radius: 50%;
    background: var(--mark-blue);
  }
  .brand-name {
    font-size: 38px;
    font-weight: 400;
    letter-spacing: 1.5px;
    color: var(--ink);
    text-transform: uppercase;
  }
  .holder {
    position: absolute;
    left: 0;
    right: 0;
    top: 212px;
    text-align: center;
    padding-left: 40px;
  }
  .holder-name {
    font-size: 42px;
    font-weight: 500;
    color: var(--name-blue);
    line-height: 1.1;
  }
  .holder-role {
    font-size: 21px;
    color: var(--ink);
    line-height: 1.1;
  }
  .contact {
    position: absolute;
    right: 36px;
    bottom: 30px;
    text-align: right;
    font-size: 21px;
    line-height: 1.27;
    color: var(--ink);
    list-style: none;
  }
</style>
</head>
<body>
  <article class="business-card">
    <span class="background-shape" aria-hidden="true"></span>
    <header class="brand">
      <span class="brand-mark" aria-hidden="true"></span>
      <span class="brand-name">Corvasta Dental</span>
    </header>
    <div class="holder">
      <p class="holder-name">Alan Morrow</p>
      <p class="holder-role">Dentist</p>
    </div>
    <ul class="contact">
      <li>740 Avenue</li>
      <li>Oregon, USA</li>
      <li>P: 555-201-4478</li>
      <li>M: 555-201-4479</li>
      <li>alanmorrow@sample.com</li>
    </ul>
  </article>
</body>
</html>
```